LSV AUDITION

I need a post card design (front only) with this on it:
Leap Spin Vibe (this is the main title to be in all caps)
Auditions
Date: Thursday June 30th
6:30-8:30 PM in person
Address: 4170 Wexley BLVD, Oakland CA 94611
video submissions turn in by Sunday July 3rd, 2022 email:LeapSpinVibe22@trovemail.net
Teens and Adults welcomed

SO PLEASE COME UP WITH A DESIGN THATS COLORFUL AND INVITING THX!

```html
<!DOCTYPE html>
<html lang="en">
<head>
<meta charset="utf-8">
<title>Leap Spin Vibe – Auditions Postcard</title>
<link rel="stylesheet" href="https://fonts.googleapis.com/css2?family=Bebas+Neue&family=Montserrat:wght@400;500;600;700;800&family=Courgette&display=swap">
<style>
  :root {
    --backdrop: #b3b3b3;
    --ink: #111111;
    --white: #ffffff;
    --pill: #1c1c1c;
    --sun: #ffd93a;
    --coral: #ff6a6f;
    --hot-pink: #ff2f9a;
    --magenta: #e040d8;
    --violet: #8a4cf0;
    --indigo: #4a50f0;
    --sky: #4fb4f0;
    --aqua: #1de9dc;
  }
  * { margin: 0; padding: 0; box-sizing: border-box; }
  html, body {
    width: 1200px; height: 958px; overflow: hidden;
    background: var(--backdrop);
  }
  .postcard {
    position: absolute; left: 65px; top: 97px;
    width: 1071px; height: 765px; overflow: hidden;
    background:
      radial-gradient(ellipse 45% 40% at 100% 12%, rgba(255,200,90,0.9), transparent 70%),
      radial-gradient(ellipse 40% 30% at 100% 50%, rgba(170,230,130,0.85), transparent 70%),
      radial-gradient(ellipse 50% 40% at 100% 100%, rgba(29,233,220,0.95), transparent 75%),
      linear-gradient(140deg, var(--sun) 0%, var(--coral) 18%, #f05fa8 32%, #d866d0 45%, #9a86e0 60%, var(--sky) 80%, var(--aqua) 100%);
  }
  .postcard__stripes {
    position: absolute; left: 0; top: 0; width: 70%; height: 100%;
    background: linear-gradient(to bottom, var(--sun) 0%, var(--hot-pink) 6%, #ff4aa0 20%, var(--magenta) 45%, var(--violet) 65%, var(--indigo) 82%, #35c8e0 92%, var(--indigo) 100%);
    -webkit-mask-image:
      repeating-linear-gradient(to bottom, #000 0 17px, transparent 17px 34px),
      linear-gradient(to right, #000 20%, transparent 95%);
    -webkit-mask-composite: source-in;
    mask-image:
      repeating-linear-gradient(to bottom, #000 0 17px, transparent 17px 34px),
      linear-gradient(to right, #000 20%, transparent 95%);
    mask-composite: intersect;
    opacity: 0.85;
  }
  .title {
    position: absolute; left: 40px; top: 62px;
    font-family: "Bebas Neue", "Oswald", sans-serif;
    font-weight: 400;
    font-size: 250px; line-height: 216px;
    color: var(--white); letter-spacing: 4px;
  }
  .title__line { display: block; }
  .info {
    position: absolute; right: 45px; text-align: right;
    font-family: "Montserrat", sans-serif; color: var(--ink);
  }
  .info__heading { top: 50px; font-size: 56px; font-weight: 600; }
  .info__when { top: 114px; font-size: 30px; line-height: 46px; font-weight: 400; }
  .venue {
    position: absolute; left: 643px; top: 243px; width: 403px; height: 62px;
    border: 2px solid var(--ink); border-top: none;
  }
  .venue::before, .venue::after {
    content: ""; position: absolute; top: 0; height: 2px; background: var(--ink);
  }
  .venue::before { left: -2px; width: 182px; }
  .venue::after { right: -2px; width: 167px; }
  .venue__pin { position: absolute; left: 196px; top: -20px; width: 28px; height: 30px; }
  .venue__address {
    position: absolute; left: 0; right: 0; top: 26px; text-align: center;
    font-family: "Montserrat", sans-serif; font-weight: 700; font-size: 16.5px; color: var(--ink);
    white-space: nowrap;
  }
  .welcome-pill {
    position: absolute; left: 654px; top: 349px; width: 420px; height: 243px;
    background: var(--pill); border-radius: 122px 0 0 122px;
  }
  .welcome-pill__line {
    position: absolute; right: 46px; white-space: nowrap;
    -webkit-background-clip: text; background-clip: text; color: transparent;
  }
  .welcome-pill__teens {
    top: 12px; font-family: "Montserrat", sans-serif; font-weight: 800; font-size: 50px;
    background-image: linear-gradient(to right, #ff5a8a, #ffa35a 60%, #ffd24a);
  }
  .welcome-pill__adults {
    top: 62px; font-family: "Montserrat", sans-serif; font-weight: 800; font-size: 96px; letter-spacing: -1px;
    background-image: linear-gradient(to right, #d86ad0, #c8a0b8 40%, #b8d08a 70%, #7ae0a0);
  }
  .welcome-pill__welcomed {
    top: 152px; font-family: "Courgette", cursive; font-size: 60px;
    background-image: linear-gradient(to right, #9a7ae0, #6aa8e0 50%, #3ad8b0);
  }
  .info__deadline { top: 605px; font-size: 25px; line-height: 34px; font-weight: 400; }
  .info__email {
    top: 688px; font-size: 19px; font-weight: 700; right: 42px;
    display: flex; align-items: center; gap: 9px;
  }
  .info__email svg { width: 18px; height: 13px; }
</style>
</head>
<body>
  <main class="postcard">
    <div class="postcard__stripes"></div>
    <h1 class="title"><span class="title__line">LEAP</span><span class="title__line">SPIN</span><span class="title__line">VIBE</span></h1>

    <h2 class="info info__heading">Auditions</h2>
    <p class="info info__when">Thursday June 30th<br>6:30-8:30 PM in person</p>

    <div class="venue">
      <svg class="venue__pin" viewBox="0 0 28 30" aria-hidden="true">
        <ellipse cx="14" cy="25" rx="12" ry="4" fill="none" stroke="#111" stroke-width="2"/>
        <path d="M14 2a7.5 7.5 0 0 0-7.5 7.5C6.5 15 14 23 14 23s7.5-8 7.5-13.5A7.5 7.5 0 0 0 14 2z" fill="#111"/>
        <circle cx="14" cy="9.5" r="2.8" fill="#f3a0a0"/>
      </svg>
      <p class="venue__address">4170 Wexley BLVD, Oakland CA 94611</p>
    </div>

    <div class="welcome-pill">
      <span class="welcome-pill__line welcome-pill__teens">Teens and</span>
      <span class="welcome-pill__line welcome-pill__adults">Adults</span>
      <span class="welcome-pill__line welcome-pill__welcomed">welcomed</span>
    </div>

    <p class="info info__deadline">video submissions turn in by<br>Sunday July 3rd, 2022</p>
    <p class="info info__email">email:LeapSpinVibe22@trovemail.net
      <svg viewBox="0 0 18 13" aria-hidden="true">
        <rect x="0" y="0" width="18" height="13" fill="#111"/>
        <path d="M0.5 0.5 9 7.5 17.5 0.5" fill="none" stroke="#9ee8d8" stroke-width="1.3"/>
      </svg>
    </p>
  </main>
</body>
</html>
```